A5 Advertising Flyer

Hi,

I need a advertising flyer. We are a die cast model car company that make replica race cars.
People send in pictures of their own cars and we replicate it or they purchase things like Corrindale Cars.
We have a new release of Vorlig 5 cars coming out as well shortly.
We make car for presents ( special occasions/ gifts,memorabilia , fund raisers, Business, collectors etc.

Below is a copy of one of our ads.

A PHOTO SPEAKS A THOUSAND WORDS BUT A REPLICA OF YOUR CAR WILL HAVE YOU TALKING FOR YEARS !

AT VORLIG3 MODEL CARS WE KNOW YOU LOVE YOUR CAR -SO WE WILL SHRINK IT FOR YOU !

Vorlig 3 is a diecast model car company founded in 1990 by Owner Damien Orsbury. Damien’s passion for all things racing was the motivation behind the Build your own Race Car concept.

Now ,POCKET YOUR RIDE , allows customers to design cars to their own requirements to start or build on their current die-cast model car collection.

In addition, these cars make a great unique gift for any occasion and have been popular for fund raising events , sponsors in the Race Car Industry and business promotion. Be quick to order as Fathers Day and Christmas is approaching fast.This gift will be straight to the pool room for sure !

Contact us today at vorlig3sales@pelmarisk.com or call 0482736194

```html
<!DOCTYPE html>
<html lang="en">
<head>
<meta charset="utf-8">
<title>Vorlig 3 Model Cars – A5 Flyer</title>
<link href="https://fonts.googleapis.com/css2?family=Oswald:wght@500;700&family=Open+Sans:wght@400;600;700&display=swap" rel="stylesheet">
<style>
  :root{
    --bg:#e9e6e2;
    --green:#2f9e3a;
    --green-dark:#1f7a2a;
    --purple:#4b2a8a;
    --yellow:#f5d21a;
    --yellow-dark:#e0a80a;
    --navy:#1d2233;
    --white:#ffffff;
    --grey:#b8b8b8;
  }
  *{box-sizing:border-box;margin:0;padding:0}
  html,body{width:833px;height:1200px;overflow:hidden;background:var(--bg)}
  body{position:relative;font-family:"Open Sans",Arial,sans-serif}
  .flyer{position:absolute;left:26px;width:780px;height:540px;background:var(--white);overflow:hidden;box-shadow:0 4px 14px rgba(0,0,0,.18)}
  .flyer--front{top:40px}
  .flyer--back{top:620px}
  .shapes{position:absolute;inset:0}
  .abs{position:absolute}
  .nowrap{white-space:nowrap}
  .photo-hero{left:0;top:0;width:380px;height:250px;background:linear-gradient(160deg,#1b2030 0%,#4a5466 55%,#9aa3ad 100%)}
  .photo-car{background:radial-gradient(ellipse at 50% 55%,#ff8a1e 0%,#e2580c 55%,rgba(226,88,12,0) 72%)}
  .heading{font-family:"Oswald",Impact,sans-serif;font-weight:700;text-transform:uppercase;line-height:1.15}
  .pill{font-family:"Oswald",Impact,sans-serif;font-weight:700;text-transform:uppercase;background:linear-gradient(#fde86a,var(--yellow) 50%,var(--yellow-dark));color:var(--navy);border-radius:20px;text-align:center;box-shadow:0 2px 3px rgba(0,0,0,.3)}
  .body-copy{font-size:12.5px;line-height:1.4;color:var(--white)}
  .badge{left:150px;top:260px;width:150px;height:150px;border-radius:50%;background:var(--purple);border:5px solid var(--white);box-shadow:0 3px 8px rgba(0,0,0,.35);text-align:center;color:var(--white);padding-top:30px}
  .badge__small{font-family:"Oswald",Impact,sans-serif;font-weight:500;font-size:20px}
  .badge__big{font-family:"Oswald",Impact,sans-serif;font-weight:700;font-size:46px;color:#6fe04a;line-height:1}
  .brand{left:26px;top:420px;font-family:"Oswald",Impact,sans-serif;font-weight:700;font-size:62px;line-height:1.1;color:var(--navy);letter-spacing:1px}
  .tagline{left:395px;top:24px;width:365px;text-align:center;color:var(--white);font-size:17px}
  .tagline .hl{color:var(--yellow);font-size:30px;display:block;margin-top:2px}
  .stamp{left:655px;top:30px;width:80px;height:95px;background:var(--grey)}
  .address-line{left:520px;width:230px;height:2px;background:#d3d3d3}
</style>
</head>
<body>

<section class="flyer flyer--front">
  <div class="abs photo-hero" role="img" aria-label="Photo of a silver sports car with glowing headlights at dusk"></div>
  <svg class="shapes" viewBox="0 0 780 540" aria-hidden="true">
    <path d="M0 215 C120 280 260 260 390 190 L390 260 C260 320 120 330 0 280 Z" fill="var(--white)"/>
    <path d="M0 235 C120 290 260 270 370 215 L370 232 C260 290 120 300 0 255 Z" fill="var(--purple)"/>
    <path d="M380 0 H760 V540 H390 C360 470 350 420 365 360 C380 300 400 250 380 0 Z" fill="var(--green)"/>
    <rect x="760" y="0" width="20" height="540" fill="var(--purple)"/>
    <path d="M0 515 C200 495 500 500 760 520 V540 H0 Z" fill="var(--green)"/>
    <path d="M0 528 C200 510 500 515 760 532 V540 H0 Z" fill="var(--purple)"/>
  </svg>

  <div class="abs badge">
    <div class="badge__small">CONTACT US</div>
    <div class="badge__big">NOW</div>
  </div>
  <div class="abs brand nowrap">VORLIG 3</div>

  <p class="abs heading tagline"><span class="nowrap">A photo speaks a thousand words</span><br><span class="nowrap">but a replica of your car will have you</span><span class="hl nowrap">Talking for years!</span></p>
  <div class="abs pill" style="left:470px;top:150px;width:230px;height:38px;line-height:38px;font-size:20px">About the company</div>
  <p class="abs body-copy" style="left:430px;top:205px;width:315px;text-align:right">Vorlig 3 is a diecast model car company founded in 1990 by Owner Damien Orsbury. Damien’s passion for all things racing was the motivation behind the Build your own Race Car concept.</p>
  <div class="abs photo-car" style="left:440px;top:300px;width:300px;height:150px" role="img" aria-label="Orange hatchback model car"></div>
  <div class="abs pill" style="left:440px;top:462px;width:290px;height:36px;line-height:36px;font-size:19px">Call us: 0482736194</div>
</section>

<section class="flyer flyer--back">
  <svg class="shapes" viewBox="0 0 780 540" aria-hidden="true">
    <path d="M0 0 H400 C440 150 470 360 430 540 H0 Z" fill="var(--green)"/>
    <path d="M0 0 H300 C200 20 80 40 0 70 Z" fill="var(--purple)"/>
    <path d="M0 500 C250 480 520 490 780 510 V540 H0 Z" fill="var(--green-dark)"/>
    <path d="M0 520 C250 502 520 510 780 526 V540 H0 Z" fill="var(--purple)"/>
  </svg>

  <p class="abs heading" style="left:20px;top:70px;width:400px;text-align:center;color:var(--white);font-size:21px">At Vorlig3 Model Cars<br>we know you love your car</p>
  <p class="abs heading nowrap" style="left:20px;top:124px;width:400px;text-align:center;color:var(--yellow);font-size:27px">So we will shrink it for you !</p>
  <div class="abs pill" style="left:90px;top:174px;width:260px;height:34px;line-height:34px;font-size:18px">Call us: 0482736194</div>
  <p class="abs body-copy" style="left:30px;top:226px;width:380px"><strong style="color:var(--yellow)">Now ,POCKET YOUR RIDE ,</strong> allows customers to design cars to their own requirements to start or build on their current die-cast model car collection.</p>
  <p class="abs body-copy" style="left:30px;top:300px;width:385px">In addition, these cars make a great unique gift for any occasion and have been popular for fund raising events , sponsors in the Race Car Industry and business promotion. Be quick to order as Fathers Day and Christmas is approaching fast.This gift will be straight to the pool room for sure !</p>
  <p class="abs heading" style="left:30px;top:430px;color:var(--white);font-size:20px">Contact us today at</p>
  <p class="abs heading nowrap" style="left:30px;top:458px;color:var(--yellow);font-size:19px">vorlig3sales@pelmarisk.com</p>

  <div class="abs stamp"></div>
  <div class="abs address-line" style="top:200px"></div>
  <div class="abs address-line" style="top:240px"></div>
  <div class="abs address-line" style="top:280px"></div>
  <div class="abs address-line" style="top:320px"></div>
  <div class="abs photo-car" style="left:520px;top:350px;width:240px;height:140px" role="img" aria-label="Orange hatchback model car"></div>
</section>

</body>
</html>
```